Website for QuillbrookCrew presentation

We need a new website, ideally as a wordpress there, for QuillbrookCrew - we focus on machine learning, big data, data science and data analytics. This website should have two main sections - team presentation, introduction and offered services as static pages, and a blog section.

Target Market(s)

Companies which would like to hire the consultants for data science

Industry/Entity Type

Data Service

Font styles to use
Sans Serif

Colors

Designer to choose colors to be used in the design.

Requirements
Must have
• Wordpress template, blog and presentation pages, nice background images, incorporate the existing logo from brief
Nice to have
• match the word and ppt existing templates for quillbrook crew

```html
<!DOCTYPE html>
<html lang="en">
<head>
<meta charset="utf-8">
<title>Quillbrook Crew</title>
<link rel="stylesheet" href="https://fonts.googleapis.com/css2?family=Montserrat:wght@500;600;700&family=Open+Sans:wght@400;600&display=swap">
<style>
:root{
  --bg:#0a85c2;
  --bg-deep:#0876b0;
  --white:#ffffff;
  --line:rgba(255,255,255,.55);
  --line-soft:rgba(255,255,255,.3);
  --accent:#0a85c2;
  --art-light:#5fb0e6;
  --art-dark:#1f5fd0;
}
*{margin:0;padding:0;box-sizing:border-box}
html,body{width:1200px;height:2687px;overflow:hidden}
body{background:var(--bg);color:var(--white);font-family:"Open Sans",Arial,sans-serif;position:relative}
.abs{position:absolute}
h1,h2,h3,.btn,.brand,.nav a{font-family:"Montserrat",Arial,sans-serif}

.brand{left:77px;top:30px;display:flex;align-items:center;gap:14px;font-weight:700;font-size:28px;line-height:30px;letter-spacing:.5px}
.brand-mark{width:26px;height:26px;background:var(--white)}
.nav{right:77px;top:58px;display:flex;gap:42px}
.nav a{color:var(--white);text-decoration:none;font-size:15px;font-weight:500;padding-bottom:14px}
.nav a.active{border-bottom:2px solid var(--white)}

.hero-title{left:77px;top:272px;font-size:45px;font-weight:700;letter-spacing:.5px}
.hero-text{left:77px;top:344px;width:480px;font-size:17px;line-height:29px}
.btn{display:flex;align-items:center;justify-content:center;background:var(--white);color:var(--accent);font-weight:700;letter-spacing:1px;border-radius:26px;text-decoration:none}
.hero-btn{left:77px;top:424px;width:218px;height:51px;font-size:21px}
.hero-art{left:600px;top:100px;width:540px;height:540px;background:radial-gradient(ellipse at 50% 55%,var(--art-light) 0%,rgba(95,176,230,.25) 45%,transparent 70%)}

.section-title{width:1200px;text-align:center;font-size:36px;font-weight:700;letter-spacing:.5px}
.service{width:380px;font-size:14px;line-height:25px}
.service h3{font-size:21px;font-weight:500;margin-bottom:8px}
.service.left{text-align:right}
.icon-ring{width:104px;height:104px;border:1.5px solid var(--line);border-radius:50%;display:flex;align-items:center;justify-content:center}
.cross-v{left:599px;top:862px;width:1px;height:68px;background:var(--line)}
.cross-h{left:565px;top:905px;width:68px;height:1px;background:var(--line)}

.about-art{left:54px;top:1182px;width:520px;height:466px;background:linear-gradient(135deg,var(--art-light),var(--art-dark));opacity:.8;border-radius:8px}
.about-title{left:647px;top:1230px;font-size:38px;line-height:52px;font-weight:700}
.about-text{left:647px;top:1346px;width:480px;font-size:14.5px;line-height:25px}
.about-text p+p{margin-top:12px}
.about-btn{left:647px;top:1533px;width:218px;height:51px;font-size:20px}

.year{left:548px;top:1786px;width:104px;height:41px;background:var(--white);color:var(--accent);font-family:"Montserrat",sans-serif;font-weight:700;font-size:20px;display:flex;align-items:center;justify-content:center}
.timeline{left:599px;top:1827px;width:1.5px;height:415px;background:var(--line)}
.dot{width:16px;height:16px;border-radius:50%;background:var(--white)}
.post{width:437px;border:1.5px solid var(--line);border-radius:12px;padding:22px 20px 20px}
.post-head{display:flex;gap:18px;align-items:flex-start;margin-bottom:14px}
.date{width:58px;height:60px;background:var(--white);color:var(--accent);text-align:center;font-family:"Montserrat",sans-serif;flex-shrink:0}
.date b{display:block;font-size:24px;line-height:34px;font-weight:600}
.date span{font-size:14px;font-weight:600}
.post h3{font-size:17.5px;font-weight:600;line-height:29px}
.post p{font-size:14px;line-height:25px}
.view-btn{left:512px;top:2242px;width:176px;height:43px;font-size:18px;border-radius:10px}

.rule{left:77px;width:1046px;height:1px;background:var(--line-soft)}
.news-form{left:319px;top:2479px;width:562px;height:45px;border:1.5px solid var(--white);border-radius:24px;display:flex;align-items:center;justify-content:space-between;padding:0 4px 0 26px;font-size:14px}
.news-btn{width:168px;height:37px;font-size:19px;border-radius:20px}
.footer-nav{top:2568px;width:1200px;display:flex;justify-content:center;gap:24px;font-size:14px}
.footer-nav span.sep{opacity:.7}
.copyright{top:2652px;width:1200px;text-align:center;font-size:14px}
</style>
</head>
<body>

<div class="abs brand"><span class="brand-mark"></span><span>QUILLBROOK<br>CREW</span></div>
<nav class="abs nav">
  <a class="active">HOME</a><a>ABOUT</a><a>SERVICES</a><a>BLOG</a><a>CONTACT</a>
</nav>

<h1 class="abs hero-title">QUILLBROOK CREW</h1>
<p class="abs hero-text">Lorem Ipsum is simply dummy text of the printing and typesetting industry. Lorem Ipsum has been the industry.</p>
<a class="abs btn hero-btn">CONTACT US</a>
<div class="abs hero-art" role="img" aria-label="Isometric illustration of a tablet with bar charts, a target, a rocket and a magnifying glass over binary digits"></div>

<h2 class="abs section-title" style="top:694px">OUR SERVICES</h2>

<div class="abs service left" style="left:52px;top:786px"><h3>Machine learning</h3><p>Lorem Ipsum is simply dummy text of the printing and typesetting industry. Lorem Ipsum has been.</p></div>
<div class="abs service" style="left:767px;top:786px"><h3>Data science</h3><p>Lorem Ipsum is simply dummy text of the printing and typesetting industry. Lorem Ipsum has been.</p></div>
<div class="abs service left" style="left:52px;top:935px"><h3>Big data</h3><p>Lorem Ipsum is simply dummy text of the printing and typesetting industry. Lorem Ipsum has been.</p></div>
<div class="abs service" style="left:767px;top:935px"><h3>Data analytics</h3><p>Lorem Ipsum is simply dummy text of the printing and typesetting industry. Lorem Ipsum has been.</p></div>

<div class="abs icon-ring" style="left:471px;top:777px">
  <svg width="54" height="40" viewBox="0 0 54 40" fill="none" stroke="#fff" stroke-width="2.5"><circle cx="18" cy="16" r="8"/><circle cx="18" cy="16" r="3"/><circle cx="38" cy="26" r="6"/><circle cx="38" cy="26" r="2"/><path d="M18 3v4M18 25v4M5 16h4M27 16h4M38 17v3M38 32v3M29 26h3M44 26h3"/></svg>
</div>
<div class="abs icon-ring" style="left:623px;top:777px">
  <svg width="46" height="46" viewBox="0 0 46 46" fill="none" stroke="#fff" stroke-width="2"><ellipse cx="23" cy="23" rx="19" ry="8"/><ellipse cx="23" cy="23" rx="19" ry="8" transform="rotate(60 23 23)"/><ellipse cx="23" cy="23" rx="19" ry="8" transform="rotate(120 23 23)"/><circle cx="23" cy="23" r="3" fill="#fff"/></svg>
</div>
<div class="abs icon-ring" style="left:471px;top:926px">
  <svg width="44" height="46" viewBox="0 0 44 46" fill="#fff" stroke="#fff" stroke-width="2"><rect x="4" y="32" width="6" height="12"/><rect x="14" y="26" width="6" height="18"/><rect x="24" y="20" width="6" height="24"/><rect x="34" y="12" width="6" height="32"/><polyline points="5,22 15,14 25,17 38,4" fill="none"/></svg>
</div>
<div class="abs icon-ring" style="left:623px;top:926px">
  <svg width="46" height="46" viewBox="0 0 46 46" fill="none" stroke="#fff" stroke-width="2.5"><circle cx="19" cy="20" r="12"/><path d="M28 29l14 14"/><polyline points="12,24 17,18 21,22 28,11" stroke-width="2"/><path d="M24 10h5v5" stroke-width="2"/></svg>
</div>
<div class="abs cross-v"></div>
<div class="abs cross-h"></div>

<div class="abs about-art" role="img" aria-label="Illustration of two people presenting a rising line chart across dashboard panels"></div>
<h2 class="abs about-title">ABOUT<br>QUILLBROOK CREW</h2>
<div class="abs about-text">
  <p>Lorem Ipsum is simply dummy text of the printing and typesetting industry. Lorem Ipsum has been the industry's standard dummy text ever since the 1500s, when an unknown printer took a galley of type and scrambled it to make a type specimen book.</p>
  <p>It has survived not only five centuries, but also the leap into electronic typesetting, remaining essentially unchanged.</p>
</div>
<a class="abs btn about-btn">KNOW MORE</a>

<h2 class="abs section-title" style="top:1714px">LATEST BLOG</h2>
<div class="abs year">2018</div>
<div class="abs timeline"></div>
<div class="abs dot" style="left:592px;top:1935px"></div>
<div class="abs dot" style="left:592px;top:2091px"></div>

<article class="abs post" style="left:77px;top:1863px">
  <div class="post-head"><div class="date"><b>20</b><span>JAN</span></div><h3>Lorem Ipsum is simply dummy text of the printing and typesetting industry.</h3></div>
  <p>Lorem Ipsum is simply dummy text of the printing and typesetting industry. Lorem Ipsum has been the industry.</p>
</article>
<article class="abs post" style="left:686px;top:2017px">
  <div class="post-head"><div class="date"><b>20</b><span>JAN</span></div><h3>Lorem Ipsum is simply dummy text of the printing and typesetting industry.</h3></div>
  <p>Lorem Ipsum is simply dummy text of the printing and typesetting industry. Lorem Ipsum has been the industry.</p>
</article>
<a class="abs btn view-btn">VIEW MORE</a>

<div class="abs rule" style="top:2373px"></div>
<h2 class="abs section-title" style="top:2414px;font-size:34px">NEWSLETTER</h2>
<div class="abs news-form"><span>Enter Your Email</span><a class="btn news-btn">SUBSCRIBE</a></div>
<nav class="abs footer-nav"><span>Home</span><span class="sep">|</span><span>About</span><span class="sep">|</span><span>Services</span><span class="sep">|</span><span>Blog</span><span class="sep">|</span><span>Contact</span></nav>
<div class="abs rule" style="top:2633px"></div>
<p class="abs copyright">©QUILLBROOK CREW- 2018. All Rights Reserved.</p>

</body>
</html>
```